We are Here! Come and Meet the Team Flyer

A clear and quirky, flyer to let local Residents know we have landed.
Based around our logo.

We avoid anything medical but rather focus on being pet-centred, warmth, approachable and community-orientated.

We pride ourselves on being cutting-edge but steer away from a cold sterile image.
Approachability, uptodate. We understandt hat pets are part of a family and we will provide the level of care that we would expect for our own pets.

Target Market(s)

Residents in the area

Industry/Entity Type

Veterinary

Font styles to use
Sans Serif

Colors
33b8a4
ffc214
0255a3

Requirements
Must have
• Logo and PERHAPS a location of Clinic indicated on the cat of the Logo.
• NOW OPEN!
• 1) Exact location of the Clinic indicated: the lefthand side of tail, near the cat's back.
• 2) Warm, quirky, Approachable
• 3) Contact details (see attached draft Poster)
• 4) Location: Silver Brook Arcade, Building 4, Mezzanine level
Should not have
• nothing medical or cliched.

```html
<!DOCTYPE html>
<html lang="en">
<head>
<meta charset="utf-8">
<title>Tail &amp; Toe Veterinary Clinic – Now Open Flyer</title>
<link href="https://fonts.googleapis.com/css2?family=Roboto+Condensed:wght@700;900&family=Lato:wght@400;700&display=swap" rel="stylesheet">
<style>
  :root {
    --orange: #e8742a;
    --teal: #33b8a4;
    --blue: #0255a3;
    --ink: #2b2b2b;
    --grey: #5c5c5c;
    --bar-grey: #6b6b6b;
    --paper: #ffffff;
    --backdrop: #f4f4f4;
  }
  * { box-sizing: border-box; margin: 0; padding: 0; }
  html, body { width: 1200px; height: 1200px; overflow: hidden; background: var(--backdrop); }
  .flyer {
    position: absolute; left: 172px; top: 0; width: 856px; height: 1200px;
    background: var(--paper); overflow: hidden; font-family: "Lato", sans-serif;
  }
  .brand {
    position: absolute; top: 52px; left: 0; width: 100%;
    display: flex; justify-content: center; align-items: center; gap: 14px;
  }
  .brand-dot { width: 46px; height: 46px; border-radius: 50%; background: var(--teal); }
  .brand-name {
    font-family: "Lato", sans-serif; font-weight: 700; font-size: 34px;
    line-height: 1; color: var(--orange); letter-spacing: 0.5px;
  }
  .hero-photo {
    position: absolute; top: 140px; left: 0; width: 100%; height: 470px;
    background:
      radial-gradient(ellipse 180px 220px at 62% 48%, #b89a7c 0%, #8a7462 45%, rgba(120,110,104,0) 100%),
      linear-gradient(180deg, #ffffff 0%, #d9d7d6 14%, #9c9694 55%, #6f6a68 100%);
  }
  .open-tag {
    position: absolute; top: 168px; left: 28px; padding: 0 18px; height: 46px;
    background: var(--teal); color: #fff; border-radius: 23px;
    font-family: "Roboto Condensed", sans-serif; font-weight: 900; font-size: 28px;
    line-height: 46px; letter-spacing: 1px;
  }
  .swoosh { position: absolute; top: 470px; left: 0; width: 856px; height: 200px; }
  .headline {
    position: absolute; top: 648px; left: 48px; width: 800px; text-align: center;
    font-family: "Roboto Condensed", sans-serif; font-weight: 900; font-size: 110px;
    line-height: 1; color: var(--orange); letter-spacing: 1px;
  }
  .subline {
    position: absolute; top: 758px; left: 20px; width: 840px; text-align: center;
    font-family: "Roboto Condensed", sans-serif; font-weight: 700; font-size: 30px;
    line-height: 32px; color: var(--grey);
  }
  .hours-band {
    position: absolute; top: 821px; left: 0; width: 100%; height: 78px;
    background: var(--blue); color: #fff; text-align: center; padding-left: 16px;
    font-family: "Roboto Condensed", sans-serif; font-weight: 700; font-size: 66px;
    line-height: 78px; letter-spacing: 1px;
  }
  .address {
    position: absolute; top: 919px; left: 0; width: 100%;
    display: flex; justify-content: center; align-items: center; gap: 8px;
    font-size: 20px; line-height: 26px; color: var(--ink);
  }
  .address-pin { width: 18px; height: 24px; flex: none; }
  .contact-rule { position: absolute; top: 997px; left: 0; width: 100%; height: 2px; background: var(--teal); }
  .contact-label {
    position: absolute; top: 977px; left: 279px; width: 297px; height: 43px;
    background: var(--teal); color: #fff; text-align: center;
    font-family: "Roboto Condensed", sans-serif; font-weight: 700; font-size: 28px; line-height: 43px;
  }
  .contact-grid { position: absolute; top: 1045px; left: 0; width: 100%; height: 118px; }
  .contact-col { position: absolute; top: 0; width: 240px; text-align: center; font-size: 18px; color: var(--ink); }
  .contact-col.col-1 { left: 95px; }
  .contact-col.col-2 { left: 305px; }
  .contact-col.col-3 { left: 525px; }
  .contact-icon { display: block; margin: 0 auto; width: 20px; height: 20px; }
  .contact-line { display: block; margin-top: 8px; height: 22px; }
  .contact-social { display: block; margin: 8px auto 0; width: 22px; height: 22px; border-radius: 50%; background: var(--teal); }
  .contact-handle { display: block; margin-top: 4px; }
  .col-divider { position: absolute; top: 1060px; width: 1px; height: 100px; background: #d6d6d6; }
  .col-divider.d1 { left: 324px; }
  .col-divider.d2 { left: 529px; }
  .footer-bar { position: absolute; bottom: 0; left: 0; width: 100%; height: 20px; background: var(--bar-grey); }
</style>
</head>
<body>
  <main class="flyer">
    <header class="brand">
      <span class="brand-dot"></span>
      <span class="brand-name">Tail &amp; Toe Veterinary Clinic</span>
    </header>

    <div class="hero-photo" role="img" aria-label="Photo of a tabby cat looking out from behind the white bars of a clinic kennel"></div>

    <div class="open-tag">NOW OPEN!</div>

    <svg class="swoosh" viewBox="0 0 856 200" preserveAspectRatio="none" aria-hidden="true">
      <path d="M0 120 Q 330 10 856 95 L856 200 L0 200 Z" fill="var(--teal)"/>
      <path d="M0 180 Q 330 40 856 110 L856 200 L0 200 Z" fill="var(--orange)"/>
      <path d="M0 190 Q 330 52 856 128 L856 200 L0 200 Z" fill="var(--paper)"/>
    </svg>

    <h1 class="headline">DID YOU KNOW?</h1>
    <p class="subline">HARBOUR CRESCENT NOW HAS ITS OWN VETERINARY CLINIC</p>

    <div class="hours-band">OPEN 7 DAYS A WEEK</div>

    <p class="address">
      <svg class="address-pin" viewBox="0 0 18 24" aria-hidden="true"><path fill="var(--orange)" d="M9 0a9 9 0 0 0-9 9c0 6.5 9 15 9 15s9-8.5 9-15a9 9 0 0 0-9-9zm0 12.5A3.5 3.5 0 1 1 9 5.5a3.5 3.5 0 0 1 0 7z"/></svg>
      <span>Mezzanine Level, Building 4, Silver Brook Arcade (Above Cafe Lumo)</span>
    </p>

    <div class="contact-rule"></div>
    <div class="contact-label">How To Contact Us?</div>

    <div class="col-divider d1"></div>
    <div class="col-divider d2"></div>

    <section class="contact-grid">
      <div class="contact-col col-1">
        <svg class="contact-icon" viewBox="0 0 24 24" aria-hidden="true"><path fill="var(--teal)" d="M6.6 10.8a15 15 0 0 0 6.6 6.6l2.2-2.2a1 1 0 0 1 1-.25 11.4 11.4 0 0 0 3.6.57 1 1 0 0 1 1 1V20a1 1 0 0 1-1 1A17 17 0 0 1 3 4a1 1 0 0 1 1-1h3.5a1 1 0 0 1 1 1c0 1.25.2 2.45.57 3.570a1 1 0 0 1-.25 1z"/></svg>
        <span class="contact-line">800-555-0147</span>
        <span class="contact-social"></span>
        <span class="contact-handle">@TailToeVetsHarbour</span>
      </div>
      <div class="contact-col col-2">
        <svg class="contact-icon" viewBox="0 0 24 24" aria-hidden="true"><path fill="var(--teal)" d="M6.6 10.8a15 15 0 0 0 6.6 6.6l2.2-2.2a1 1 0 0 1 1-.25 11.4 11.4 0 0 0 3.6.57 1 1 0 0 1 1 1V20a1 1 0 0 1-1 1A17 17 0 0 1 3 4a1 1 0 0 1 1-1h3.5a1 1 0 0 1 1 1c0 1.25.2 2.45.57 3.57a1 1 0 0 1-.25 1z"/></svg>
        <span class="contact-line">04 555 0192</span>
        <span class="contact-social"></span>
        <span class="contact-handle">@tailtoevet</span>
      </div>
      <div class="contact-col col-3">
        <svg class="contact-icon" viewBox="0 0 24 24" aria-hidden="true"><circle cx="12" cy="12" r="9" fill="none" stroke="var(--teal)" stroke-width="2.5"/></svg>
        <span class="contact-line">www.tailandtoevet.example</span>
        <span class="contact-social"></span>
        <span class="contact-handle">@tailtoeclinic</span>
      </div>
    </section>

    <div class="footer-bar"></div>
  </main>
</body>
</html>
```